Business card design for online Mandarin Learning School

We need a business card design for our online language learning school called "Sunny Kite Academy for Mandarin Learning". Our existing website is https://www.sunnykiteacademy.com
We have our logo already. We would like to see our business card design that can make our online teaching services to be innovative, young, energetic and fun to learn. Prefer to have a certain level of color matching with our website. Apart from "Sunny Kite Academy", need to specifically state "for Mandarin Learning" as well on the business card.

```html
<!DOCTYPE html>
<html lang="en">
<head>
<meta charset="utf-8">
<title>Sunny Kite Academy – Business Card</title>
<link rel="stylesheet" href="https://fonts.googleapis.com/css2?family=Noto+Sans:wght@400;600&display=swap">
<style>
  :root {
    --coral: #e25f5f;
    --teal: #1aabb6;
    --ink: #111111;
    --figure-grey: #858585;
    --paper: #ffffff;
    --backdrop: #ffffff;
  }
  * { margin: 0; padding: 0; box-sizing: border-box; }
  html, body {
    width: 1200px;
    height: 1200px;
    overflow: hidden;
    background: var(--backdrop);
    font-family: "Noto Sans", sans-serif;
    color: var(--ink);
  }
  .canvas { position: relative; width: 1200px; height: 1200px; }

  .card {
    position: absolute;
    left: 130px;
    width: 918px;
    overflow: hidden;
  }
  .card-front { top: 62px; height: 461px; }
  .card-back  { top: 638px; height: 458px; }

  .card-bg { position: absolute; inset: 0; width: 100%; height: 100%; display: block; }

  /* Front */
  .figure-art {
    position: absolute;
    border-radius: 46% 54% 40% 60%;
    background: radial-gradient(ellipse at center, rgba(133,133,133,0.55), rgba(133,133,133,0.15) 70%, rgba(133,133,133,0) 100%);
  }
  .figure-art-left  { left: 60px;  top: 10px; width: 320px; height: 300px; }
  .figure-art-right { left: 640px; top: 0;    width: 278px; height: 290px; }

  .brand {
    position: absolute;
    left: 0; right: 0;
    top: 250px;
    display: flex;
    flex-direction: column;
    align-items: center;
    gap: 26px;
  }
  .brand-dot {
    width: 54px; height: 54px;
    border-radius: 50%;
    background: var(--paper);
  }
  .brand-name {
    font-size: 50px;
    font-weight: 600;
    letter-spacing: 1px;
    color: var(--ink);
    white-space: nowrap;
  }

  /* Back */
  .role {
    position: absolute;
    left: 23px; top: 20px;
    font-size: 30px;
  }
  .teachers {
    position: absolute;
    left: 25px; top: 98px;
    list-style: none;
    font-size: 32px;
    line-height: 41px;
    letter-spacing: 0.5px;
  }
  .skills {
    position: absolute;
    left: 690px; top: 22px;
    list-style: none;
    font-size: 42px;
    line-height: 54px;
    transform: rotate(5deg);
    transform-origin: left top;
  }
  .skills li:nth-child(2) { margin-left: -8px; }
  .skills li:nth-child(3) { margin-left: -14px; }
  .skills li:nth-child(4) { margin-left: -20px; }

  .mission {
    position: absolute;
    left: 38px; top: 224px;
    width: 760px;
    font-size: 22px;
    line-height: 26px;
    letter-spacing: 0.6px;
    transform: rotate(5deg);
    transform-origin: left top;
  }
  .website {
    position: absolute;
    left: 5px; top: 392px;
    font-size: 32px;
    letter-spacing: 0.5px;
    transform: rotate(3deg);
    transform-origin: left top;
  }
</style>
</head>
<body>
<main class="canvas">

  <section class="card card-front" aria-label="Business card front">
    <svg class="card-bg" viewBox="0 0 918 461" preserveAspectRatio="none" aria-hidden="true">
      <rect width="918" height="461" fill="var(--coral)"/>
      <polygon points="522,0 918,0 918,461 398,461" fill="var(--teal)"/>
    </svg>
    <div class="figure-art figure-art-left" role="img" aria-label="Faint grey figures of cheering children"></div>
    <div class="figure-art figure-art-right" role="img" aria-label="Faint grey figures of cheering children"></div>
    <div class="brand">
      <span class="brand-dot" aria-hidden="true"></span>
      <h1 class="brand-name">Sunny Kite Academy</h1>
    </div>
  </section>

  <section class="card card-back" aria-label="Business card back">
    <svg class="card-bg" viewBox="0 0 918 458" preserveAspectRatio="none" aria-hidden="true">
      <rect width="918" height="458" fill="var(--paper)"/>
      <polygon points="0,0 918,0 918,302 0,190" fill="var(--coral)"/>
      <polygon points="0,190 918,302 918,451 0,362" fill="var(--teal)"/>
    </svg>

    <p class="role">Teacher</p>
    <ul class="teachers">
      <li>Ms Mei Tan</li>
      <li>Ms Lin Zhou</li>
    </ul>

    <ul class="skills">
      <li>listening</li>
      <li>speaking</li>
      <li>reading</li>
      <li>writing</li>
    </ul>

    <p class="mission">Sunny Kite Academy for Mandarin Learning creates a flexible, convenient and comfortable learning environment to enable our students for online studying Mandarin, anytime and anywhere.</p>

    <p class="website">www.sunnykiteacademy.com</p>
  </section>

</main>
</body>
</html>
```